Marcus T Orwell DDS (dentist) needs a business card/business logo design

I would like an eye-catchingly conservative or elegant graphic presentation of my business name with the elements: prevention, restoration, and cosmetics (these are the services I'd like to emphasize) .
The business card would have room for address lines, phone and fax, web address. No standard teeth or oral representations please. Should communicate professionalism. Whatever color scheme works.

Thank you

Target Market(s)

I just want a good looking business card

Industry/Entity Type

Conservative

Contact Information for Business Card

Adress: 4716 Wrenfield Ave Lakewood CA 90642 Phone: 562 413 9082 FAX 562 413 5527 Web: Fairbrookdental.example

Font styles to use
Sans Serif

Colors
0255a3

Requirements
Must have
• business name with the elements: prevention, restoration, and cosmetics (these are the services I'd like to emphasize)
• communicates professionalism
Nice to have
• eye catching but not flashy graphics
Should not have
• no pictures of teeth or dental instruments

```html
<!DOCTYPE html>
<html lang="en">
<head>
<meta charset="utf-8">
<title>Marcus T Orwell DDS – Business Card</title>
<link href="https://fonts.googleapis.com/css2?family=Ubuntu:wght@400;500;700&display=swap" rel="stylesheet">
<style>
  :root {
    --brand-blue: #0a6cb8;
    --brand-deep: #0255a3;
    --card-white: #ffffff;
    --page-bg: #e9ecef;
  }
  * { margin: 0; padding: 0; box-sizing: border-box; }
  html, body { width: 1200px; height: 1000px; overflow: hidden; }
  body {
    background: var(--page-bg);
    font-family: 'Ubuntu', Arial, sans-serif;
    color: var(--brand-blue);
    position: relative;
  }
  .business-card {
    position: absolute;
    left: 75px; top: 200px;
    width: 1050px; height: 600px;
    background: var(--card-white);
    overflow: hidden;
    box-shadow: 0 4px 18px rgba(0,0,0,.12);
  }
  .brand-name {
    position: absolute;
    right: 50px; top: 48px;
    font-size: 56px; font-weight: 700;
    color: var(--brand-blue);
    letter-spacing: -0.5px;
    white-space: nowrap;
  }
  .side-tab {
    position: absolute;
    left: 0; top: 160px;
    width: 22px; height: 96px;
    background: var(--brand-blue);
  }
  .person-icon {
    position: absolute;
    left: 38px; top: 162px;
    width: 60px; height: 90px;
  }
  .name-pill {
    position: absolute;
    left: 112px; top: 148px;
    width: 490px; height: 116px;
    background: var(--brand-blue);
    border-radius: 0 50px 50px 0;
    color: var(--card-white);
    padding: 18px 54px 0 28px;
  }
  .name-pill .full-name {
    display: block;
    font-size: 33px; font-weight: 700;
    white-space: nowrap;
    line-height: 1.15;
  }
  .name-pill .job-title {
    display: block;
    font-size: 25px; font-weight: 400;
    text-align: right;
    line-height: 1.2;
    margin-top: 6px;
  }
  .tagline {
    position: absolute;
    right: 28px; top: 214px;
    font-size: 24px; font-weight: 500;
    white-space: nowrap;
  }
  .tagline-rule {
    position: absolute;
    left: 596px; right: 0; top: 254px;
    height: 4px; background: var(--brand-blue);
  }
  .contact-line {
    position: absolute;
    display: flex; align-items: center; gap: 10px;
    font-size: 25px; font-weight: 500;
    white-space: nowrap;
    line-height: 1.2;
  }
  .contact-line svg { width: 30px; height: 30px; flex: none; }
  .contact-phone { left: 42px; top: 292px; }
  .contact-fax { left: 42px; top: 342px; }
  .contact-web { left: 370px; top: 384px; }
  .contact-address { left: 370px; top: 432px; }
  .footer-band { position: absolute; left: 0; bottom: 0; width: 1050px; height: 110px; }
</style>
</head>
<body>
  <main class="business-card">
    <div class="brand-name">Orwell Dental</div>

    <div class="side-tab"></div>
    <svg class="person-icon" viewBox="0 0 60 90" aria-hidden="true">
      <circle cx="30" cy="20" r="16" fill="var(--brand-blue)"/>
      <path d="M4 88 V58 Q4 40 22 40 H38 Q56 40 56 58 V88 Z" fill="var(--brand-blue)"/>
      <path d="M26 40 H34 L32 48 L35 74 L30 80 L25 74 L28 48 Z" fill="#fff"/>
    </svg>

    <div class="name-pill">
      <span class="full-name">Marcus T Orwell DDS</span>
      <span class="job-title">Dentist</span>
    </div>

    <div class="tagline">Prevention, Restoration and Cosmetics</div>
    <div class="tagline-rule"></div>

    <div class="contact-line contact-phone">
      <svg viewBox="0 0 30 30" aria-hidden="true">
        <path d="M3 11 Q15 2 27 11 L24 15 L20 13 V10 Q15 8 10 10 V13 L6 15 Z" fill="var(--brand-blue)"/>
        <path d="M9 15 H21 L25 26 H5 Z" fill="var(--brand-blue)"/>
        <circle cx="15" cy="20" r="3" fill="#fff"/>
      </svg>
      <span>: 562- 413- 9082</span>
    </div>
    <div class="contact-line contact-fax">
      <svg viewBox="0 0 30 30" aria-hidden="true">
        <rect x="8" y="3" width="14" height="8" fill="var(--brand-blue)"/>
        <rect x="3" y="11" width="24" height="11" rx="2" fill="var(--brand-blue)"/>
        <rect x="8" y="18" width="14" height="9" fill="#fff" stroke="var(--brand-blue)" stroke-width="2"/>
      </svg>
      <span>: 562- 413- 5527</span>
    </div>
    <div class="contact-line contact-web">
      <svg viewBox="0 0 30 30" aria-hidden="true">
        <circle cx="15" cy="15" r="13" fill="var(--brand-blue)"/>
        <text x="15" y="18" font-size="8" font-family="Ubuntu, sans-serif" font-weight="700" fill="#fff" text-anchor="middle">www</text>
      </svg>
      <span>: www.Fairbrookdental.example</span>
    </div>
    <div class="contact-line contact-address">
      <svg viewBox="0 0 30 30" aria-hidden="true">
        <path d="M15 3 A7 7 0 0 1 22 10 Q22 15 15 22 Q8 15 8 10 A7 7 0 0 1 15 3 Z" fill="none" stroke="var(--brand-blue)" stroke-width="2.5"/>
        <circle cx="15" cy="10" r="2.5" fill="var(--brand-blue)"/>
        <path d="M3 27 L7 20 H11 M19 20 H23 L27 27 Z" fill="none" stroke="var(--brand-blue)" stroke-width="2"/>
      </svg>
      <span>: 4716 Wrenfield Ave, Lakewood, CA 90642</span>
    </div>

    <svg class="footer-band" viewBox="0 0 1050 110" preserveAspectRatio="none" aria-hidden="true">
      <rect x="0" y="4" width="1050" height="6" fill="var(--brand-blue)"/>
      <path d="M0 30 H780 Q820 30 840 22 Q870 10 900 14 H1050 V110 H0 Z" fill="var(--brand-blue)"/>
      <path d="M0 26 H780 Q820 26 840 18 Q870 6 900 10 H1050" fill="none" stroke="#fff" stroke-width="4"/>
    </svg>
  </main>
</body>
</html>
```